Product labels for new supplements business targeting high performing creative people

I need a label design for different supplements like Whey, BCAA, Melatonin etc. that I could customize for each use case separately.

The brand is called wovenpath.life, and it would be the first design of the labels. We haven't sold any products yet, but the target audience is people with growth mindset, people who want to be as efficient as possible and are constantly looking to improve their lifestyle. As part of that, they are also working out, but don't know much about supplements yet. Mostly people between 20-34.

I don't have a too specific idea of the expected design, though it should be light, warm, smart and minimalist, maybe have some patterns. It should looks smart and clean (and expensive). Orange and golden might be the additional colors for white. I have attached the templates of some products that I plan to sell and also the logo of the brand.

Here's what I have used for inspiration:
Brands that I like and are somewhat similar in concept: https://www.plarnix.com/ (!!specially the way they
bring "how the product helps them" in focus, not "what the product is" & https://www.bevo.care/ &
https://www.moflesta.com/sport/ & https://en.calwostor.fr/ &
https://artboardhub.com/profiles/mirelfondastudio/designs/461827

Here's how different products look like: https://bondrexa.com/catalog

Target Market(s)

target audience is people with growth mindset, people who want to be as efficient as possible and are constantly looking to improve their lifestyle. As part of that, they are also working out, but don't know much about supplements yet. Mostly people between 20-34.

Industry/Entity Type

Supplements

Font styles to use
Sans Serif

Colors
FFC000
F8CF3A
FAE287
FDF2CF
FEFAEE
F0912C
F2A743
F7CA91
FBE8D2
FDF5EE
EE7325
F08F49
F5BC92
FAE3D3
FDF4ED

Requirements
Must have
• Clean, smart and minimalist design that can be applied for different products in different sizes, like Whey protein, BCAA, vitamins etc. available here: https://bondrexa.com/catalog
Nice to have
• Patterns, expensive look
Should not have
• Doodles, too many colors

```html
<!DOCTYPE html>
<html lang="en">
<head>
<meta charset="utf-8">
<title>wovenpath.life — Supplement Labels</title>
<link rel="stylesheet" href="https://fonts.googleapis.com/css2?family=Montserrat:ital,wght@0,400;0,500;0,600;1,400&display=swap">
<style>
  :root {
    --backdrop: #ffdbc1;
    --label: #ffffff;
    --ink: #1f1f1f;
    --orange: #f07318;
    --orange-deep: #ee4a22;
    --orange-soft: #f08f49;
    --edge: #f3e4d8;
  }
  * { box-sizing: border-box; margin: 0; padding: 0; }
  html, body { width: 800px; height: 1200px; overflow: hidden; }
  body {
    position: relative;
    background: var(--backdrop);
    font-family: "Montserrat", sans-serif;
    color: var(--ink);
  }
  .label {
    position: absolute;
    background: var(--label);
    border: 1px solid var(--edge);
    border-radius: 6px;
    display: flex;
    flex-direction: column;
    align-items: center;
    text-align: center;
  }
  .brand {
    display: flex;
    align-items: center;
    gap: 0.35em;
    font-weight: 600;
    color: var(--ink);
    letter-spacing: -0.01em;
  }
  .brand-mark {
    width: 0.7em;
    height: 0.7em;
    background: var(--orange);
  }
  .product-name {
    font-weight: 500;
    line-height: 0.95;
    color: transparent;
    -webkit-text-stroke: 1px var(--orange-deep);
    text-transform: uppercase;
  }
  .variant-band {
    background: var(--orange);
    color: #fff;
    font-weight: 500;
    text-transform: uppercase;
  }
  .benefits {
    display: flex;
    align-items: center;
    gap: 4px;
    text-align: left;
    font-style: italic;
    color: var(--orange-soft);
    line-height: 1.25;
  }
  .benefit-icon { flex: none; stroke: var(--ink); fill: none; stroke-width: 1.4; }
  .net-weight { color: var(--orange-deep); }
  .supplement-band {
    background: var(--orange);
    color: #fff;
    text-transform: uppercase;
    letter-spacing: 0.35em;
  }

  /* Melatonin */
  .label--melatonin { left: 185px; top: 185px; width: 136px; height: 180px; padding-top: 20px; }
  .label--melatonin .brand { font-size: 11px; }
  .label--melatonin .product-name { font-size: 23px; margin-top: 18px; width: 80px; text-align: left; }
  .label--melatonin .variant-band { width: 90px; font-size: 9px; padding: 4px 0; margin-top: 3px; }
  .label--melatonin .benefits { font-size: 6px; margin-top: 20px; }
  .label--melatonin .supplement-band { width: 84px; font-size: 4px; padding: 2px 0; margin-top: 6px; letter-spacing: 0.3em; }
  .tablet-count {
    position: absolute; right: 8px; top: 122px;
    font-size: 4px; color: var(--orange); letter-spacing: 0.1em;
    writing-mode: vertical-rl; transform: rotate(180deg);
  }

  /* Beef protein */
  .label--protein { left: 462px; top: 470px; width: 212px; height: 200px; padding-top: 27px; }
  .label--protein .brand { font-size: 17px; }
  .label--protein .product-name { font-size: 23px; margin-top: 18px; width: 106px; text-align: left; }
  .label--protein .variant-band { width: 110px; font-size: 9px; padding: 5px 0; margin-top: 3px; letter-spacing: 0.3em; }
  .label--protein .benefits { font-size: 5.5px; margin-top: 12px; }
  .label--protein .net-weight { font-size: 7px; margin-top: 14px; }
  .label--protein .supplement-band { width: 110px; font-size: 4.5px; padding: 2px 0; margin-top: 5px; }

  /* BCAA */
  .label--bcaa { left: 142px; top: 810px; width: 256px; height: 300px; padding-top: 50px; }
  .label--bcaa .brand { font-size: 20px; }
  .label--bcaa .product-name { font-size: 29px; margin-top: 28px; letter-spacing: 0.22em; text-align: left; width: 112px; line-height: 1; }
  .label--bcaa .variant-band { width: 134px; font-size: 11px; padding: 5px 0; margin-top: 3px; letter-spacing: 0.3em; }
  .label--bcaa .benefits { font-size: 7.5px; margin-top: 38px; }
  .label--bcaa .net-weight { font-size: 8px; margin-top: 18px; }
  .label--bcaa .supplement-band { width: 134px; font-size: 5.5px; padding: 3px 0; margin-top: 6px; }
</style>
</head>
<body>

  <section class="label label--melatonin" aria-label="Melatonin label">
    <div class="brand"><span class="brand-mark"></span>wovenpath.life</div>
    <h2 class="product-name">Mela-<br>tonin</h2>
    <div class="variant-band">1 MG</div>
    <div class="benefits">
      <svg class="benefit-icon" width="11" height="11" viewBox="0 0 12 12"><path d="M7 1.5a5 5 0 1 0 3.8 7.6A4.2 4.2 0 0 1 7 1.5z"/></svg>
      <p>Fall asleep faster<br>Stay asleep longer</p>
    </div>
    <div class="supplement-band">Dietary supplement</div>
    <span class="tablet-count">60 TABLETS</span>
  </section>

  <section class="label label--protein" aria-label="Beef protein label">
    <div class="brand"><span class="brand-mark"></span>wovenpath.life</div>
    <h2 class="product-name">Beef<br>Protein</h2>
    <div class="variant-band">Chocolate</div>
    <div class="benefits">
      <svg class="benefit-icon" width="16" height="16" viewBox="0 0 16 16"><circle cx="8" cy="8" r="6"/></svg>
      <p>Hydrolyzed beef protein with minimum fat content<br>Promotes muscle gain and helps maintain muscle mass</p>
    </div>
    <p class="net-weight">NET Wt. 900g</p>
    <div class="supplement-band">Dietary supplement</div>
  </section>

  <section class="label label--bcaa" aria-label="BCAA label">
    <div class="brand"><span class="brand-mark"></span>wovenpath.life</div>
    <h2 class="product-name">BCAA<br>2:1:1</h2>
    <div class="variant-band">Wild berry</div>
    <div class="benefits">
      <svg class="benefit-icon" width="14" height="14" viewBox="0 0 14 14"><polygon points="7,1 12,4 12,10 7,13 2,10 2,4"/></svg>
      <p>Essential branched chain amino acids BCAA<br>Increasses muscle growth, reduces fatique</p>
    </div>
    <p class="net-weight">NET Wt. 300g</p>
    <div class="supplement-band">Dietary supplement</div>
  </section>

</body>
</html>
```